Business Card Design Project

Need a business card with logo that is attached.
Company name: Tolmen Brisk Solutions, LLC
My name: Lorna Tolmen
Title: President
Phone number: 703-555-0148
Email: ltolmen@tolmenbrisksolutions.example
web site: www.tolmenbrisksolutions.example

Industry/Entity Type

Business

```html
<!DOCTYPE html>
<html lang="en">
<head>
<meta charset="utf-8">
<title>Tolmen Brisk Solutions, LLC — Business Card</title>
<link rel="stylesheet" href="https://fonts.googleapis.com/css2?family=Cinzel:wght@400;500&family=Questrial&display=swap">
<style>
  :root {
    --backdrop: #eceef0;
    --card: #ffffff;
    --ink: #111111;
    --teal: #2a9d8c;
    --teal-deep: #1f8a86;
    --blue: #2d3f9e;
    --blue-mid: #2a6fb8;
    --rule: #2a9d8c;
  }
  * { margin: 0; padding: 0; box-sizing: border-box; }
  html, body {
    width: 1200px;
    height: 801px;
    overflow: hidden;
    background: var(--backdrop);
  }
  .canvas {
    position: relative;
    width: 1200px;
    height: 801px;
  }
  .card {
    position: absolute;
    left: 75px;
    top: 100px;
    width: 1050px;
    height: 600px;
    background: var(--card);
    box-shadow: 0 6px 24px rgba(0, 0, 0, 0.12);
    overflow: hidden;
  }
  .swooshes {
    position: absolute;
    inset: 0;
    width: 100%;
    height: 100%;
  }
  .brand {
    position: absolute;
    left: 58px;
    top: 150px;
    display: flex;
    align-items: center;
    gap: 18px;
  }
  .brand-mark {
    width: 92px;
    height: 92px;
    border-radius: 50%;
    background: var(--teal-deep);
  }
  .brand-rule {
    width: 2px;
    height: 112px;
    background: var(--rule);
  }
  .brand-name {
    font-family: "Cinzel", serif;
    font-weight: 400;
    font-size: 27px;
    line-height: 32px;
    color: var(--teal-deep);
  }
  .person {
    position: absolute;
    left: 300px;
    top: 268px;
    text-align: right;
  }
  .person-name {
    font-family: "Cinzel", serif;
    font-weight: 500;
    font-size: 46px;
    line-height: 52px;
    color: var(--ink);
  }
  .person-title {
    font-family: "Cinzel", serif;
    font-weight: 400;
    font-size: 24px;
    line-height: 26px;
    color: var(--ink);
    margin-right: 4px;
  }
  .contact {
    position: absolute;
    right: 58px;
    top: 352px;
    text-align: right;
    font-family: "Questrial", sans-serif;
    color: var(--ink);
  }
  .contact-phone {
    font-size: 27px;
    line-height: 36px;
  }
  .contact-line {
    font-size: 17px;
    line-height: 24px;
  }
</style>
</head>
<body>
<div class="canvas">
  <section class="card">
    <svg class="swooshes" viewBox="0 0 1050 600" aria-hidden="true">
      <defs>
        <linearGradient id="swoosh-top" x1="0" y1="0" x2="1" y2="0">
          <stop offset="0" stop-color="var(--teal)"/>
          <stop offset="0.55" stop-color="var(--blue-mid)"/>
          <stop offset="1" stop-color="var(--blue)"/>
        </linearGradient>
        <linearGradient id="swoosh-bottom" x1="1" y1="0" x2="0" y2="0">
          <stop offset="0" stop-color="var(--teal)"/>
          <stop offset="0.5" stop-color="var(--blue-mid)"/>
          <stop offset="1" stop-color="var(--blue)"/>
        </linearGradient>
      </defs>
      <path class="swoosh-top" fill="url(#swoosh-top)"
            d="M 440 118 Q 720 250 880 0 L 985 0 Q 800 330 440 118 Z"/>
      <path class="swoosh-bottom" fill="url(#swoosh-bottom)"
            d="M 560 498 Q 280 400 70 600 L 175 600 Q 330 430 560 498 Z"/>
    </svg>

    <div class="brand">
      <span class="brand-mark" aria-hidden="true"></span>
      <span class="brand-rule" aria-hidden="true"></span>
      <p class="brand-name">Tolmen Brisk<br>Solutions<br>LLC</p>
    </div>

    <div class="person">
      <h1 class="person-name">Lorna Tolmen</h1>
      <p class="person-title">President</p>
    </div>

    <address class="contact">
      <p class="contact-phone">703-555-0148</p>
      <p class="contact-line">ltolmen@tolmenbrisksolutions.example</p>
      <p class="contact-line">www.tolmenbrisksolutions.example</p>
    </address>
  </section>
</div>
</body>
</html>
```